Cardiology Practice needs a Heart Scan Order Form

Busy cardiology practice needs an order form for a heart scan test. Sample is attached. One side should have all information noted and the other side should have our physician names (Vikram Joshi, MD, K.L. Morvandi, MD, Anjali Desai, MD, Parvin Joshi, MD, and Gerald Montefino, MD. It should have the map that is uploaded and our demographic information (Crestline Cardio PLLC, 218 Juniper Ave. Ste. B, Webster, TX 77412 along with phone 713-642-1187 and fax 713-642-1188) as well as our web address (crestlinecardio.example). Our primary colors are red, black and white. Needs to fit paper size 8 1/2 by 11.

Target Market(s)

Healthcare

Industry/Entity Type

Health Care

Font styles to use
Serif

Colors
ec1f27

Requirements
Must have
• Logo, information listed on sample form, demographics and physician names as well as website.
Nice to have
• Open to suggestions
Should not have
• Physician Pictures

```html
<!DOCTYPE html>
<html lang="en">
<head>
<meta charset="utf-8">
<title>Crestline Cardio – Calcium Score Heart Scan Order Form</title>
<link rel="stylesheet" href="https://fonts.googleapis.com/css2?family=Merriweather:wght@700;900&family=Source+Serif+4:wght@400;600;700&display=swap">
<style>
  :root {
    --brand-red: #c9343d;
    --brand-red-bright: #ec1f27;
    --ink: #1d1d1f;
    --rule: #9a9a9a;
    --field-grey: #e4e4e4;
    --paper: #ffffff;
    --backdrop: #e8e8e8;
    --card-dark: #2a2a2c;
    --map-base: #eceef0;
    --display: "Merriweather", Georgia, serif;
    --text: "Source Serif 4", Georgia, serif;
  }
  * { box-sizing: border-box; margin: 0; padding: 0; }
  html, body { width: 900px; height: 1200px; overflow: hidden; }
  body { background: var(--backdrop); font-family: var(--text); color: var(--ink); position: relative; }
  .sheet {
    position: absolute; left: 232px; width: 436px; height: 564px;
    background: var(--paper); box-shadow: 0 2px 8px rgba(0,0,0,.18);
    display: flex; flex-direction: column; overflow: hidden;
  }
  .sheet--front { top: 20px; }
  .sheet--back { top: 616px; }

  /* ---------- front: order form ---------- */
  .form-body { flex: 1; padding: 14px 18px 12px; display: flex; flex-direction: column; justify-content: space-between; }
  .form-header { display: flex; align-items: flex-start; gap: 10px; }
  .brand { display: flex; align-items: center; gap: 5px; padding-top: 8px; width: 112px; }
  .brand__dot { width: 12px; height: 12px; border-radius: 50%; background: var(--brand-red-bright); flex: none; }
  .brand__name { font-family: var(--display); font-weight: 900; font-size: 10.5px; color: var(--brand-red-bright); line-height: 1.1; text-transform: uppercase; }
  .form-title { font-family: var(--display); font-weight: 900; font-size: 13.5px; line-height: 1.15; text-transform: uppercase; padding-top: 4px; flex: 1; }
  .schedule { width: 122px; border: 1px solid var(--rule); font-size: 6.5px; }
  .schedule__head { background: var(--field-grey); text-align: center; padding: 1px 0; }
  .schedule__row { display: flex; border-top: 1px solid var(--rule); height: 11px; align-items: center; padding-left: 3px; }
  .schedule__row span { width: 32px; border-right: 1px solid var(--rule); height: 100%; line-height: 11px; }

  .physician-band { background: var(--brand-red); color: #fff; font-family: var(--text); font-weight: 700; font-size: 6.8px; display: flex; justify-content: space-between; padding: 3px 8px; }

  .info-grid { display: grid; grid-template-columns: 1fr 1fr; gap: 8px; }
  .field-table { border: 1px solid var(--rule); font-size: 6.5px; }
  .field-table__head { background: var(--field-grey); text-align: center; font-weight: 600; padding: 1px 0; }
  .field-row { display: flex; border-top: 1px solid var(--rule); height: 14px; }
  .field-row > div { flex: 1; border-right: 1px solid var(--rule); padding: 1px 3px; white-space: nowrap; }
  .field-row > div:last-child { border-right: 0; }
  .field-row .narrow { flex: 0 0 30px; }

  .section-bar { background: var(--field-grey); text-align: center; font-weight: 700; font-size: 7.5px; padding: 2px 0; }
  .vitals { display: flex; gap: 6px; font-size: 6.5px; }
  .vitals .box { border: 1px solid var(--rule); height: 13px; display: flex; align-items: center; padding-left: 3px; flex: 1; }
  .vitals .box--sex { flex: 0 0 84px; justify-content: space-between; padding-right: 12px; }

  .diagnosis { font-size: 6.8px; }
  .diagnosis__line { display: flex; gap: 4px; align-items: flex-end; margin-bottom: 6px; }
  .diagnosis__line i { flex: 1; border-bottom: 1px solid var(--ink); height: 7px; }
  .checklist { display: grid; grid-template-columns: repeat(4, 1fr); row-gap: 5px; }
  .check { display: flex; align-items: center; gap: 3px; white-space: nowrap; }
  .check::before { content: ""; width: 6px; height: 6px; border: 1px solid var(--ink); flex: none; }

  .instructions { font-size: 6.8px; line-height: 1.5; }
  .instructions h3 { font-size: 7.4px; font-weight: 700; margin-bottom: 3px; }
  .instructions ul { list-style: none; }
  .instructions li { display: flex; gap: 4px; }
  .instructions li::before { content: ""; width: 5px; height: 5px; border: 1px solid var(--ink); margin-top: 3px; flex: none; }

  .acknowledge { font-size: 6.8px; line-height: 1.5; }
  .sign-off { display: grid; grid-template-columns: 1.3fr 1fr; gap: 10px; align-items: end; }
  .signatures { display: grid; grid-template-columns: 1fr 1fr; column-gap: 10px; row-gap: 10px; font-size: 6.8px; font-weight: 600; }
  .signatures div { border-top: 1px solid var(--ink); padding-top: 2px; margin-top: 14px; }
  .referral .field-row > div:first-child { flex: 0 0 42px; }

  .form-footer { background: var(--brand-red); color: #fff; font-size: 7px; text-align: center; padding: 10px 20px; line-height: 1.5; }

  /* ---------- back: physicians & map ---------- */
  .back-body { flex: 1; padding: 16px 20px 12px; display: flex; flex-direction: column; gap: 10px; }
  .back-title { background: var(--brand-red); color: #fff; font-family: var(--display); font-weight: 900; font-size: 12px; text-align: center; padding: 5px 0; text-transform: uppercase; }
  .physician-cards { display: grid; grid-template-columns: repeat(5, 1fr); gap: 5px; }
  .physician-card { background: var(--card-dark); color: #fff; padding: 8px 2px; text-align: center; border-top: 3px solid var(--brand-red); }
  .physician-card__name { font-family: var(--text); font-weight: 700; font-size: 7px; white-space: nowrap; }
  .physician-card__role { font-size: 5.8px; opacity: .85; margin-top: 2px; }
  .map-area { flex: 1; border: 1px solid #c9c9c9; background: linear-gradient(135deg, #f1e6c4 0%, var(--map-base) 30%, var(--map-base) 70%, #dfe4e8 100%); }
  .back-footer { background: var(--brand-red); color: #fff; font-size: 7px; display: flex; justify-content: space-between; align-items: center; padding: 12px 20px; }
  .contact { display: flex; align-items: center; gap: 3px; white-space: nowrap; }
  .contact svg { width: 8px; height: 8px; fill: none; stroke: #fff; stroke-width: 1.4; }
</style>
</head>
<body>

<section class="sheet sheet--front">
  <div class="form-body">
    <header class="form-header">
      <div class="brand"><span class="brand__dot"></span><span class="brand__name">Crestline<br>Cardio</span></div>
      <h1 class="form-title">Calcium Score<br>Heart Scan</h1>
      <div class="schedule">
        <div class="schedule__head">Test schedule</div>
        <div class="schedule__row"><span>Test date:</span></div>
        <div class="schedule__row"><span>Test time:</span></div>
      </div>
    </header>

    <div class="physician-band">
      <span>Vikram Joshi, M.D.</span><span>K.L. Morvandi, M.D.</span><span>Anjali Desai, M.D.</span><span>Parvin Joshi, M.D.</span><span>Gerald Montefino, M.D.</span>
    </div>

    <div class="info-grid">
      <div class="field-table">
        <div class="field-table__head">Patient information</div>
        <div class="field-row"><div>Last name</div><div>First name</div><div class="narrow">MI</div></div>
        <div class="field-row"><div>Date of birth</div><div>Account no.</div></div>
      </div>
      <div class="field-table">
        <div class="field-table__head">Contact information</div>
        <div class="field-row"><div>Address:</div></div>
        <div class="field-row"><div>Home phone no.</div><div>Mobile phone no.</div></div>
      </div>
    </div>

    <div class="section-bar">Medical information</div>
    <div class="vitals">
      <div class="box box--sex"><span>Sex:</span><span>F</span><span>M</span></div>
      <div class="box">Height:</div>
      <div class="box">Weight:</div>
      <div class="box">Race:</div>
    </div>

    <div class="diagnosis">
      <div class="diagnosis__line"><span>Diagnosis:</span><i></i></div>
      <div class="checklist">
        <span class="check">PCI (no. of stents: ____)</span>
        <span class="check">CABG (no. of vessels: ____)</span>
        <span class="check">MI (last event: ____)</span>
        <span class="check">PCM/ICD</span>
        <span class="check">Diabetes</span>
        <span class="check">Claustrophobia</span>
        <span class="check">Asthma</span>
        <span class="check">COPD</span>
        <span class="check">LMP: ________</span>
        <span class="check">bHCG</span>
        <span class="check">Tubal ligation</span>
        <span class="check">Hysterectomy</span>
        <span></span><span></span>
        <span class="check">Emphysema</span>
        <span class="check">Post-menopause &gt; 1 year</span>
      </div>
    </div>

    <div class="instructions">
      <h3>Please read the following instructions carefully. You might be rescheduled if any of the following instructions are not met.</h3>
      <ul>
        <li>AVOID caffeine containing products (coffee, tea, soda, chocolate, energy drinks, or some over the counter medications) for 4 hours prior to testing.</li>
        <li>AVOID smoking for 4 hours prior to testing.</li>
        <li>AVOID eating or drinking anything except water for 4 hours prior to testing.</li>
        <li>Arrive 15 minutes early for your appointment time.</li>
        <li>Wear comfortable clothing. Remove any metal objects, such as jewelry or piercings. Women will be asked to remove bras containing metal underwire.</li>
        <li>Inform your physician or the staff if you are claustrophobic or have a problem staying in restricted environments for any length of time.</li>
        <li>Inform the physician or the staff if you are or think you might be pregnant.</li>
      </ul>
    </div>

    <p class="acknowledge">I hereby acknowledge that the instructions and procedures pertinent to this study were explained thoroughly, I had time to ask questions, and these questions were addressed satisfactorily.</p>

    <div class="sign-off">
      <div class="signatures">
        <div>Patient's print name</div><div>Patient's signature</div>
        <div>Prescriber's print name</div><div>Prescriber's signature</div>
      </div>
      <div class="field-table referral">
        <div class="field-table__head">Referring physician contact information</div>
        <div class="field-row"><div>Order date:</div><div></div></div>
        <div class="field-row"><div>Tel no.:</div><div></div></div>
        <div class="field-row"><div>Fax no.:</div><div></div></div>
      </div>
    </div>
  </div>
  <footer class="form-footer">
    Crestline Cardio PLLC. Visit us at 218 Juniper Ave. Ste. B, Webster, TX 77412. For appointments or more information on testing, please call 713-642-1187, or visit www.crestlinecardio.example.
  </footer>
</section>

<section class="sheet sheet--back">
  <div class="back-body">
    <h2 class="back-title">Our Physician Names</h2>
    <div class="physician-cards">
      <article class="physician-card"><div class="physician-card__name">Vikram Joshi, MD</div><div class="physician-card__role">Cardiovascular Medicine</div></article>
      <article class="physician-card"><div class="physician-card__name">K.L. Morvandi, MD</div><div class="physician-card__role">Cardiovascular Medicine</div></article>
      <article class="physician-card"><div class="physician-card__name">Anjali Desai, MD</div><div class="physician-card__role">Cardiovascular Medicine</div></article>
      <article class="physician-card"><div class="physician-card__name">Parvin Joshi, MD</div><div class="physician-card__role">Cardiovascular Disease</div></article>
      <article class="physician-card"><div class="physician-card__name">Gerald Montefino, MD</div><div class="physician-card__role">Cardiovascular Disease</div></article>
    </div>
    <div class="map-area" role="img" aria-label="Street map of Webster, TX showing the practice location and nearby roads"></div>
  </div>
  <footer class="back-footer">
    <span class="contact"><svg viewBox="0 0 10 10"><path d="M5 9.5C5 9.5 1.8 6 1.8 4a3.2 3.2 0 0 1 6.4 0C8.2 6 5 9.5 5 9.5z"/><circle cx="5" cy="4" r="1.1"/></svg>218 Juniper Ave., Suite B, Webster, TX</span>
    <span class="contact"><svg viewBox="0 0 10 10"><path d="M2 1h2l1 2.5-1.3 1a5 5 0 0 0 2.8 2.8l1-1.3L10 7v2a1 1 0 0 1-1 1A8 8 0 0 1 1 2a1 1 0 0 1 1-1z"/></svg>713-642-1187</span>
    <span class="contact"><svg viewBox="0 0 10 10"><rect x="1" y="4" width="8" height="5"/><rect x="3" y="1" width="4" height="3"/></svg>713-642-1188</span>
    <span class="contact"><svg viewBox="0 0 10 10"><circle cx="5" cy="5" r="4"/><path d="M1 5h8M5 1c2 2.5 2 5.5 0 8M5 1c-2 2.5-2 5.5 0 8"/></svg>www.crestlinecardio.example</span>
  </footer>
</section>

</body>
</html>
```